GHollis Busisness Card

I am an aerospace consultant and at this time only need business cards.

Industry/Entity Type

Business

Contact Information for Business Card

Hollis Partners,LLC
Gerald T. Hollis

348 Birch Hollow Road
Madison AL 35762

256-555-0148 (cell)
256-555-0173 (fax)

geraldhollis@mailbrook.net

```html
<!DOCTYPE html>
<html lang="en">
<head>
<meta charset="utf-8">
<title>Hollis Partners – Business Card</title>
<link href="https://fonts.googleapis.com/css2?family=Lato:wght@400;700;900&display=swap" rel="stylesheet">
<style>
  :root {
    --page-bg: #2b2b2b;
    --card-white: #ffffff;
    --card-grey: #e6e6e6;
    --brand-red: #d10a0a;
    --brand-red-dark: #b00000;
    --ink: #1f1f1f;
    --on-red: #ffffff;
  }
  html, body {
    margin: 0;
    width: 1200px;
    height: 900px;
    overflow: hidden;
    background: var(--page-bg);
    font-family: "Lato", sans-serif;
  }
  .business-card {
    position: absolute;
    left: 180px;
    top: 210px;
    width: 840px;
    height: 480px;
    border-radius: 28px;
    overflow: hidden;
    background: linear-gradient(160deg, var(--card-white) 0%, #f4f4f4 55%, var(--card-grey) 100%);
  }
  .header-band {
    position: absolute;
    left: 0; top: 0;
    width: 100%;
    height: 92px;
    background: linear-gradient(180deg, var(--brand-red) 0%, var(--brand-red-dark) 100%);
  }
  .person {
    position: absolute;
    right: 34px;
    top: 16px;
    text-align: right;
    color: var(--on-red);
  }
  .person-name {
    font-weight: 900;
    font-size: 30px;
    letter-spacing: 0.5px;
    line-height: 1.1;
  }
  .person-title {
    font-size: 18px;
    font-weight: 400;
    margin-top: 2px;
  }
  .company {
    position: absolute;
    left: 0; width: 100%;
    top: 160px;
    text-align: center;
  }
  .company-rule {
    display: block;
    width: 420px;
    height: 3px;
    margin: 0 auto;
    background: linear-gradient(90deg, transparent, var(--brand-red) 30%, var(--brand-red) 70%, transparent);
  }
  .company-name {
    font-weight: 900;
    font-size: 46px;
    color: var(--brand-red);
    letter-spacing: 0.5px;
    margin: 16px 0;
    line-height: 1;
  }
  .contact-left {
    position: absolute;
    left: 24px;
    right: 370px;
    top: 360px;
    text-align: right;
  }
  .contact-right {
    position: absolute;
    left: 490px;
    top: 318px;
  }
  .contact-line {
    display: flex;
    align-items: center;
    gap: 10px;
    font-size: 21px;
    font-weight: 700;
    color: var(--ink);
    height: 36px;
    white-space: nowrap;
  }
  .contact-left .contact-line { justify-content: flex-end; }
  .icon { width: 21px; height: 21px; flex: none; fill: var(--ink); }
</style>
</head>
<body>
  <section class="business-card">
    <div class="header-band">
      <div class="person">
        <div class="person-name">GERALD T. HOLLIS</div>
        <div class="person-title">Aerospace Consultant</div>
      </div>
    </div>

    <div class="company">
      <span class="company-rule"></span>
      <div class="company-name">HOLLIS PARTNERS</div>
      <span class="company-rule"></span>
    </div>

    <div class="contact-left">
      <div class="contact-line">256-555-0148
        <svg class="icon" viewBox="0 0 24 24" aria-label="mobile"><rect x="6" y="2" width="12" height="20" rx="2" fill="none" stroke="#1f1f1f" stroke-width="2"/><rect x="10" y="18" width="4" height="1.6"/></svg>
      </div>
      <div class="contact-line">348 Birch Hollow Road Madison AL 35762
        <svg class="icon" viewBox="0 0 24 24" aria-label="address"><path d="M12 3 1 13h3v8h6v-5h4v5h6v-8h3z"/></svg>
      </div>
    </div>

    <div class="contact-right">
      <div class="contact-line">
        <svg class="icon" viewBox="0 0 24 24" aria-label="fax"><rect x="6" y="3" width="12" height="6"/><rect x="2" y="9" width="20" height="9" rx="2"/><rect x="6" y="15" width="12" height="6" fill="#fff" stroke="#1f1f1f" stroke-width="2"/></svg>
        256-555-0173
      </div>
      <div class="contact-line">
        <svg class="icon" viewBox="0 0 24 24" aria-label="email"><rect x="2" y="5" width="20" height="14"/><path d="M2 5l10 8 10-8" fill="none" stroke="#fff" stroke-width="1.8"/></svg>
        geraldhollis@mailbrook.net
      </div>
    </div>
  </section>
</body>
</html>
```